National Rent-to-Own sheds company needs new coded front end web page

HBX Summit provides a rent-to-own financing option to storage building dealers in the southeast U.S. We need a redesign of HBX Summit's front end web site.

Current site is https://www.hbxsummit.example/

I'm looking to get a coded (HTML & CSS) single page design. I am a PHP developer and looking to outsource the design of the front end of the site. You don't have to make anything work beyond HTML and CSS. I would like the layout to be done in Bootstrap and as such the CSS would already be done. You would just have to add your supplemental CSS for whatever background, colors, fonts, or custom elements that need to be styled.

The client's website does not have a whole lot of content, as you can see if you visit the page, so I'd like to turn the current front-end with multiple pages into a single page. Most of the content is quite short and I'd like an artful way to present it. I'd like to actually remove the menu at the top.

See this site for examples of Bootstrap layouts: https://quiltgrid.example/themes/business?branch=3.x

If all goes well with this project, we would like to continue to work with the designer in the near future on some other similar projects.
Updates

I have updated the brief for single page design clarification.

The About Us page is a duplicate of the home page, so you can ignore that. The Rental Programs offered are actually 24, 36, 48, and 60. The FAQs page we will probably link to a modal window, so don't worry about its content; we just need a way to provide the link to it. The contact page info could use some nice styling. The Dealer Login page should become a single button like the Customer Payments at the top.

Industry/Entity Type

Building

Font styles to use
Sans Serif

Colors

Designer to choose colors to be used in the design.

Requirements
Must have
• The new design should be marked up with Bootstrap 3. It should be a responsive layout. The HTML, CSS, and any image assets should be provided. A PSD or other design file is not required, but we'll certainly take it if you made one anyway.

Clean, simple design.
Nice to have
• Some stock photography may help to explain in a glance what HBX Summit does. Some keywords to look for in stock photos: storage buildings, storage sheds, backyard storage, rent-to-own, barns. Note that you don't need to purchase the stock photos. Just use watermarked placeholders in your layout.

```html
<!DOCTYPE html>
<html lang="en">
<head>
<meta charset="utf-8">
<title>HBX Summit — Rent-to-Own Storage Buildings</title>
<link rel="stylesheet" href="https://fonts.googleapis.com/css2?family=Open+Sans:wght@400;600;700;800&display=swap">
<style>
:root{
  --navy:#0f2f69;
  --navy-deep:#0a2352;
  --orange:#f39a1e;
  --ink:#2f2f2f;
  --muted:#5c5c5c;
  --paper:#ffffff;
  --mist:#f0f0f0;
  --rule:#3a3a3a;
  --footer:#2a2a2a;
  --footer-text:#d8d8d8;
}
*{box-sizing:border-box;margin:0;padding:0}
html,body{width:1200px;height:2504px;overflow:hidden}
body{font-family:"Open Sans",Arial,sans-serif;color:var(--ink);background:var(--paper);position:relative}
.icon{display:inline-block;vertical-align:middle;fill:currentColor}

/* header */
.site-header{position:absolute;left:0;top:0;width:1200px;height:160px;background:var(--paper)}
.account-links{position:absolute;right:120px;top:0;display:flex;background:#222;height:28px}
.account-links a{color:#fff;font-size:12px;font-weight:600;text-decoration:none;padding:0 14px;line-height:28px}
.account-links a+a{border-left:1px solid #555}
.brand{position:absolute;left:150px;top:34px;display:flex;align-items:center;gap:14px}
.brand-mark{width:22px;height:22px;background:var(--orange)}
.brand-name{font-size:46px;font-weight:800;color:var(--navy);letter-spacing:-1px}
.call-us{position:absolute;right:140px;top:52px;text-align:right}
.call-us .label{font-size:18px;font-weight:700;color:#222}
.call-us .number{display:flex;align-items:center;gap:12px;font-size:30px;font-weight:600;color:#222;margin-top:2px}
.call-us .ring{width:36px;height:36px;border:2px solid #333;border-radius:50%;display:flex;align-items:center;justify-content:center;color:#333}

/* hero */
.hero{position:absolute;left:0;top:160px;width:1200px;height:440px;background:linear-gradient(180deg,#8d9489 0%,#6f776c 55%,#59604f 100%)}
.hero-frame{position:absolute;left:152px;top:40px;width:896px;height:360px;border:6px solid #f4f4f4;background:linear-gradient(120deg,#c9c2b4 0%,#a7a597 35%,#9b3a28 62%,#6f8c4c 100%)}
.hero-tagline{position:absolute;left:24px;top:20px;background:rgba(40,40,40,.78);color:#fff;padding:14px 22px;font-size:28px;font-weight:700;line-height:1.25}

/* showcase band */
.showcase{position:absolute;left:0;top:600px;width:1200px;height:248px;background:var(--navy-deep)}
.showcase-tile{position:absolute;top:32px;width:264px;height:192px;border:4px solid #f4f4f4}
.tile-1{left:152px;background:linear-gradient(160deg,#d9dfe6,#b7bcc0 60%,#7f8f6a)}
.tile-2{left:468px;background:linear-gradient(160deg,#d8b98c,#a9743d 60%,#6d8a48)}
.tile-3{left:784px;background:linear-gradient(160deg,#d9d4cc,#b9a590 55%,#7d8fa4)}

/* section headings */
.section-title{position:absolute;left:0;width:1200px;height:44px}
.section-title::before{content:"";position:absolute;left:0;right:0;top:21px;height:3px;background:var(--rule)}
.section-title h2{position:absolute;left:112px;top:0;padding:0 16px;font-size:30px;font-weight:800;line-height:44px;color:#222;background:var(--bg,#fff)}

/* about */
.about-title{top:916px}
.about-photo{position:absolute;left:152px;top:1000px;width:264px;height:160px;background:linear-gradient(135deg,#d6b27a,#a07848 50%,#6b6b6b)}
.about-copy{position:absolute;left:448px;top:996px;width:600px;font-size:14px;line-height:1.6;color:var(--muted)}
.about-copy p+p{margin-top:14px}

/* rental plans */
.rental{position:absolute;left:0;top:1248px;width:1200px;height:344px;background:linear-gradient(180deg,#7b7b7b,#a3a3a3 45%,#8a8a8a)}
.rental-title{position:absolute;left:432px;top:28px;width:336px;height:44px;background:rgba(255,255,255,.85);text-align:center;font-size:26px;font-weight:700;line-height:44px;color:#333}
.rental-note{position:absolute;left:200px;top:84px;width:800px;text-align:center;font-size:12px;font-weight:600;line-height:1.5;color:#fff}
.plans{position:absolute;left:144px;top:176px;display:flex;gap:24px}
.plan{position:relative;width:216px;height:108px;background:#fdfdfd;border:1px solid #ccc;box-shadow:0 3px 8px rgba(0,0,0,.25);text-align:center;padding-top:44px;font-size:30px;font-weight:700;color:#333}
.plan .clock{position:absolute;left:80px;top:-30px;width:56px;height:56px;border-radius:50%;background:#1e5fa8;border:3px solid #fff;color:#fff;display:flex;align-items:center;justify-content:center}

/* contact */
.contact{position:absolute;left:0;top:1592px;width:1200px;height:768px;background:var(--mist)}
.contact-title{top:80px;--bg:var(--mist)}
.contact-cols{position:absolute;left:140px;top:170px;display:flex;gap:40px}
.contact-col{width:280px}
.contact-col h3{display:flex;align-items:center;gap:12px;font-size:20px;font-weight:700;font-variant:small-caps;color:#222;margin-bottom:22px}
.contact-col h3 .badge{width:32px;height:32px;border-radius:50%;background:var(--orange);color:#fff;display:flex;align-items:center;justify-content:center}
.line{display:flex;align-items:flex-start;gap:10px;font-size:14px;line-height:20px;color:var(--muted);margin-bottom:18px}
.line .icon{color:var(--orange);margin-top:2px;flex:none}
.line strong{color:#333;font-weight:600}

/* footer */
.site-footer{position:absolute;left:0;top:2360px;width:1200px;height:144px;background:var(--footer);color:var(--footer-text)}
.footer-info{position:absolute;left:152px;top:18px;font-size:14px;line-height:1.3}
.footer-info .row{display:flex;align-items:center;gap:12px;margin-bottom:8px}
.footer-info .icon{color:#fff}
.footer-map{position:absolute;left:448px;top:16px;width:240px;height:112px;background:linear-gradient(135deg,#e8e6df,#d4d9cf 60%,#c9d3dc)}
.footer-legal{position:absolute;right:152px;top:20px;font-size:12px;text-align:right;line-height:1.5}
</style>
</head>
<body>
<svg width="0" height="0" style="position:absolute" aria-hidden="true">
  <symbol id="i-phone" viewBox="0 0 24 24"><path d="M6.6 10.8a15 15 0 0 0 6.6 6.6l2.2-2.2a1 1 0 0 1 1-.25 11.4 11.4 0 0 0 3.6.57 1 1 0 0 1 1 1V20a1 1 0 0 1-1 1A17 17 0 0 1 3 4a1 1 0 0 1 1-1h3.5a1 1 0 0 1 1 1c0 1.25.2 2.45.57 3.57a1 1 0 0 1-.25 1z"/></symbol>
  <symbol id="i-mail" viewBox="0 0 24 24"><path d="M3 5h18a1 1 0 0 1 1 1v12a1 1 0 0 1-1 1H3a1 1 0 0 1-1-1V6a1 1 0 0 1 1-1zm1 2.3V17h16V7.3l-8 5.2z M4.6 7h14.8L12 11.8z"/></symbol>
  <symbol id="i-pin" viewBox="0 0 24 24"><path d="M12 2a7 7 0 0 1 7 7c0 5-7 13-7 13S5 14 5 9a7 7 0 0 1 7-7zm0 4.5A2.5 2.5 0 1 0 12 11.5 2.5 2.5 0 0 0 12 6.5z"/></symbol>
  <symbol id="i-fax" viewBox="0 0 24 24"><path d="M6 2h9l3 3v4H6zM3 10h18v9h-3v3H6v-3H3zm5 7v3h8v-3z"/></symbol>
  <symbol id="i-clock" viewBox="0 0 24 24"><path d="M12 2a10 10 0 1 1 0 20 10 10 0 0 1 0-20zm0 2.2a7.8 7.8 0 1 0 0 15.6 7.8 7.8 0 0 0 0-15.6zM11 6h2v5.6l3.6 2.1-1 1.7L11 12.8z"/></symbol>
  <symbol id="i-user" viewBox="0 0 24 24"><circle cx="12" cy="8" r="4"/><path d="M4 21c0-4.4 3.6-7 8-7s8 2.6 8 7z"/></symbol>
  <symbol id="i-card" viewBox="0 0 24 24"><path d="M2 6a1 1 0 0 1 1-1h18a1 1 0 0 1 1 1v12a1 1 0 0 1-1 1H3a1 1 0 0 1-1-1zm2 2v2h16V8zm0 5v4h16v-4z"/></symbol>
</svg>

<header class="site-header">
  <nav class="account-links"><a href="#">Dealer Login</a><a href="#">Customer Payments</a></nav>
  <div class="brand"><span class="brand-mark"></span><span class="brand-name">HBX Summit</span></div>
  <div class="call-us">
    <div class="label">CALL US NOW!</div>
    <div class="number"><span class="ring"><svg class="icon" width="18" height="18"><use href="#i-phone"/></svg></span>555-014-2160</div>
  </div>
</header>

<section class="hero">
  <div class="hero-frame" role="img" aria-label="Smiling family in front of a red backyard storage shed">
    <div class="hero-tagline">Why page offsite storage?<br>When you can rent to own!</div>
  </div>
</section>

<section class="showcase">
  <div class="showcase-tile tile-1" role="img" aria-label="White storage building with grey roof"></div>
  <div class="showcase-tile tile-2" role="img" aria-label="Wooden storage barn on a lawn"></div>
  <div class="showcase-tile tile-3" role="img" aria-label="Couple reviewing a payment plan together"></div>
</section>

<div class="section-title about-title"><h2>ABOUT US</h2></div>
<div class="about-photo" role="img" aria-label="Builder assembling a storage building"></div>
<div class="about-copy">
  <p>HBX Summit provides affordable alternatives for your storage needs. Unlike off-site self storage, HBX Summit provides a path to ownership. As an industry leader, we partner with proven, successful storage building retailers and manufacturers to provide quality storage - in your backyard.</p>
  <p>We are pioneers in providing flexible payment options so you can match a rental plan to fit your storage building needs. Ask your retailer about our 24, 36, 48, and 60 month payment options. Why rent self-storage when you can rent-to-own!</p>
</div>

<section class="rental" role="region" aria-label="Rental plans">
  <div class="rental-title">RENTAL PLANS</div>
  <p class="rental-note">Match the rental plan with the storage building that fits your needs. As a leader in providing creative, affordable storage solutions, HBX Summit offers a rent-to-own term made for you. Every plan comes with no early payoff penalty.</p>
  <div class="plans">
    <div class="plan"><span class="clock"><svg class="icon" width="30" height="30"><use href="#i-clock"/></svg></span>24 MONTHS</div>
    <div class="plan"><span class="clock"><svg class="icon" width="30" height="30"><use href="#i-clock"/></svg></span>36 MONTHS</div>
    <div class="plan"><span class="clock"><svg class="icon" width="30" height="30"><use href="#i-clock"/></svg></span>48 MONTHS</div>
    <div class="plan"><span class="clock"><svg class="icon" width="30" height="30"><use href="#i-clock"/></svg></span>60 MONTHS</div>
  </div>
</section>

<section class="contact">
  <div class="section-title contact-title"><h2>CONTACT INFORMATION</h2></div>
  <div class="contact-cols">
    <div class="contact-col">
      <h3><span class="badge"><svg class="icon" width="18" height="18"><use href="#i-phone"/></svg></span>Dealer Support</h3>
      <div class="line"><svg class="icon" width="16" height="16"><use href="#i-phone"/></svg><span>555-014-2162</span></div>
      <div class="line"><svg class="icon" width="16" height="16"><use href="#i-mail"/></svg><span><strong>Maren - ext 2</strong><br>maren@hbxsummit.example</span></div>
      <div class="line"><svg class="icon" width="16" height="16"><use href="#i-mail"/></svg><span><strong>Tessa - ext 1</strong><br>tessa@hbxsummit.example</span></div>
    </div>
    <div class="contact-col">
      <h3><span class="badge"><svg class="icon" width="18" height="18"><use href="#i-user"/></svg></span>Outside Sales Reps</h3>
      <div class="line"><svg class="icon" width="16" height="16"><use href="#i-phone"/></svg><span>555-014-2162</span></div>
      <div class="line"><svg class="icon" width="16" height="16"><use href="#i-mail"/></svg><span><strong>Corin Vale</strong><br>corin@hbxsummit.example<br>SC, NC, VA and Eastern TN</span></div>
      <div class="line"><svg class="icon" width="16" height="16"><use href="#i-mail"/></svg><span><strong>Wade Ellison</strong><br>wade@hbxsummit.example<br>GA, FL, AL</span></div>
      <div class="line"><svg class="icon" width="16" height="16"><use href="#i-mail"/></svg><span><strong>Hal Brenner</strong><br>hal@hbxsummit.example<br>MS, LA, AR, Western TN</span></div>
      <div class="line"><svg class="icon" width="16" height="16"><use href="#i-mail"/></svg><span><strong>Reid Tolman</strong><br>reid@hbxsummit.example<br>TX, OK</span></div>
    </div>
    <div class="contact-col">
      <h3><span class="badge"><svg class="icon" width="18" height="18"><use href="#i-card"/></svg></span>Payment Center</h3>
      <div class="line"><svg class="icon" width="16" height="16"><use href="#i-phone"/></svg><span>555-017-3034</span></div>
      <div class="line"><svg class="icon" width="16" height="16"><use href="#i-mail"/></svg><span><strong>Nora - ext 1</strong><br>nora@hbxsummit.example</span></div>
      <div class="line"><svg class="icon" width="16" height="16"><use href="#i-mail"/></svg><span><strong>Ivy - ext 2</strong><br>ivy@hbxsummit.example</span></div>
      <div class="line"><svg class="icon" width="16" height="16"><use href="#i-mail"/></svg><span><strong>June - ext 3</strong><br>june@hbxsummit.example</span></div>
      <div class="line"><svg class="icon" width="16" height="16"><use href="#i-mail"/></svg><span><strong>Lena - ext 4</strong><br>lena@hbxsummit.example</span></div>
      <div class="line"><svg class="icon" width="16" height="16"><use href="#i-mail"/></svg><span><strong>Faye - ext 6</strong><br>faye@hbxsummit.example</span></div>
    </div>
  </div>
</section>

<footer class="site-footer">
  <div class="footer-info">
    <div class="row"><svg class="icon" width="18" height="18"><use href="#i-pin"/></svg><span>P.O. Box 4410<br>Harlow, SC 29000</span></div>
    <div class="row"><svg class="icon" width="16" height="16"><use href="#i-phone"/></svg><span>555-014-2160</span></div>
    <div class="row"><svg class="icon" width="16" height="16"><use href="#i-fax"/></svg><span>555-019-5199</span></div>
    <div class="row"><svg class="icon" width="16" height="16"><use href="#i-mail"/></svg><span>info@hbxsummit.example</span></div>
  </div>
  <div class="footer-map" role="img" aria-label="Street map showing the office location"></div>
  <div class="footer-legal">Copyright © 2011 HBX Summit.<br>All Rights Reserved.</div>
</footer>
</body>
</html>
```